Childrens Business Card Design Project

We have an existing logo attached which we'd like to use as part of our new business card design.

The design needs to be relatively gender neutral and contain bright colours.

In terms of look and feel think:

Fun, Modern, Quality (as opposed to cheap!) and of course Party!

Single or double sided - i am not decided on either one yet - ideally i'd like to see designs for both because if you think stylistically it would benefit having two sides then please try it out!

I think the challenge here is finding a really good background colour (if you think it needs one) and also choosing an eye grabbing text that compliments the existing logo - do that an you are onto a winner! I have another image for the business (which i have attached) which uses stripes so i am keen to see a design that incorporates this to tie in all my collateral.

The copy required is as follows (not necesarily in this order)

Bookings/Enquiries:

Tilda

T: 0498 217 503
E: enquiries@brightfoxparties.example.au

ABN: 47 302 658 114

Any feedback on text is welcomed - please message me or add to the discussion.

Reason: Hi All, I have received some promising designs, but overall i am not impressed with the quality of the work so have extended the deadline as this project has been committed. I will aim to attach some business card examples to the brief tomorrow to give further guidance as a whole but please do not submit any designs on a generic background that are not related to the theme, have been carelessly placed with overlapping elements - it just looks sloppy. For those who have read the brief an incorporated stripes or even spots this is on target as it convey's a party theme, however please work on getting the colours for the contact details by either a bold solid strip to highlight or some other way to frame it. When it comes to the logo, some people have removed the characters all together and changed the colour of the wording - this is fine. Also feel free to balloons starts - but keep it classy and watch your placement of these. I hope this helps and for the designs i would like to see revisions for i will aim to get back to you individually over the next day or so. Many thanks all.

Target Market(s)

Mothers in the suburbs of Australia with a disposal able income, children aged between 1-7 years old.

Industry/Entity Type

Business

Requirements
Must have
• The font and wording positioning must compliment the logo.

```html
<!DOCTYPE html>
<html lang="en">
<head>
<meta charset="utf-8">
<title>Bright Fox Parties – Business Card</title>
<link rel="stylesheet" href="https://fonts.googleapis.com/css2?family=Kalam:wght@400;700&family=Andika:wght@700&display=swap">
<style>
  :root {
    --backdrop: #a4a998;
    --card-pink: #e8268d;
    --logo-blue: #2b93d9;
    --tagline-orange: #f6a31c;
    --ink-dark: #2a1030;
    --ink-light: #ffffff;
    --art-warm: #f3b0c9;
    --art-mid: #f7d36b;
    --art-cool: #9fd1ec;
    --bunting-yellow: #f4e23a;
    --bunting-blue: #3bb5e0;
    --bunting-purple: #6b3fa0;
  }
  html, body {
    margin: 0;
    padding: 0;
    width: 1200px;
    height: 960px;
    overflow: hidden;
    background: var(--backdrop);
  }
  .canvas {
    position: relative;
    width: 1200px;
    height: 960px;
  }
  .card {
    position: absolute;
    width: 600px;
    height: 340px;
    background: var(--card-pink);
    overflow: hidden;
    box-shadow: 0 6px 16px rgba(0,0,0,0.18);
  }
  .card--front { left: 90px; top: 110px; }
  .card--back { left: 510px; top: 510px; }

  /* Front */
  .character-art {
    position: absolute;
    left: 70px;
    top: 30px;
    width: 460px;
    height: 165px;
    border-radius: 14px;
    background: linear-gradient(90deg, var(--art-warm), var(--art-mid) 50%, var(--art-cool));
    opacity: 0.85;
  }
  .brand-name {
    position: absolute;
    left: 0;
    right: 0;
    top: 206px;
    margin: 0;
    text-align: center;
    font-family: "Kalam", cursive;
    font-weight: 700;
    font-size: 56px;
    line-height: 1;
    color: var(--logo-blue);
  }
  .brand-tagline {
    position: absolute;
    right: 92px;
    top: 280px;
    margin: 0;
    font-family: "Andika", sans-serif;
    font-weight: 700;
    font-size: 15px;
    letter-spacing: 0.5px;
    color: var(--tagline-orange);
  }

  /* Back */
  .bunting-art {
    position: absolute;
    left: 0;
    top: 20px;
    width: 64px;
    height: 120px;
    border-radius: 0 60px 60px 0;
    background: linear-gradient(180deg, var(--bunting-yellow), var(--bunting-blue) 45%, var(--bunting-purple));
    opacity: 0.8;
  }
  .balloon-art {
    position: absolute;
    right: 30px;
    top: 14px;
    width: 280px;
    height: 215px;
    border-radius: 20px;
    background: linear-gradient(135deg, rgba(242,226,28,0.55), rgba(229,42,42,0.6) 35%, rgba(43,90,168,0.6) 70%, rgba(102,184,50,0.55));
  }
  .contact {
    position: absolute;
    left: 40px;
    top: 160px;
    font-family: "Kalam", cursive;
    color: var(--ink-light);
  }
  .contact__label {
    margin: 0;
    font-size: 26px;
    font-weight: 400;
    color: var(--ink-dark);
    line-height: 1.1;
  }
  .contact__name {
    margin: 2px 0 4px;
    font-size: 40px;
    font-weight: 700;
    line-height: 1.05;
  }
  .contact__line {
    margin: 0;
    font-size: 21px;
    line-height: 1.4;
  }
</style>
</head>
<body>
<main class="canvas">

  <section class="card card--front" aria-label="Business card front">
    <div class="character-art" role="img" aria-label="Illustration of a cartoon fairy, a clown doing a handstand and a pirate child"></div>
    <h1 class="brand-name">Bright Fox Parties</h1>
    <p class="brand-tagline">Kids Parties &amp; Events</p>
  </section>

  <section class="card card--back" aria-label="Business card back">
    <div class="bunting-art" role="img" aria-label="Fan of colourful party bunting flags"></div>
    <div class="balloon-art" role="img" aria-label="Bunch of colourful party balloons"></div>
    <div class="contact">
      <p class="contact__label">Bookings/Enquiries:</p>
      <p class="contact__name">Tilda</p>
      <p class="contact__line">T: 0498 217 503</p>
      <p class="contact__line">E: enquiries@brightfoxparties.example.au</p>
    </div>
  </section>

</main>
</body>
</html>
```